RLW CONSTRUCTION CO POSTCARD DESIGN

I was thinking of making a postcard for mailings by printmoor and or by me dropping off at homes . I guess it would be used as a mailing post card and or flyer . I have had sketch harbor design my buisnes cards . The buisness card design is a different version from my signage on trucks because of space . I have a logo design . thyat i can upload . I like silver for back ground and black for logo and letters with glossy finish . I would like to have the RLW with a back drop to give it depth , it would be the same color as windows .

The file i submitted ha a design with red letters , this design is more detailed than the other and should be used . The colors should be black on a silver card glossy . The windows and maybe give the letters depth with a backdrop outline . I want to let home owners know that they can always call for consultation and and repairs or maintenance for their home .

Target Market(s)

home owners

Industry/Entity Type

Construction

Other font styles liked:
• The same font as used in the picture of the sign i uploaded

Requirements
Must have
• HOME IMPROVEMENTS , MAINTENANCE AND REPAIRS , CARPENTRY , TILE PAINTING ECT

```html
<!DOCTYPE html>
<html lang="en">
<head>
<meta charset="utf-8">
<title>RLW Construction Co. Postcard</title>
<link href="https://fonts.googleapis.com/css2?family=EB+Garamond:wght@400;600&display=swap" rel="stylesheet">
<style>
  :root {
    --stage: #262626;
    --card-white: #ffffff;
    --panel-grey: #b9b9b9;
    --panel-text: #4a4a4a;
    --bar-dark: #3a3a3a;
    --bar-dark-end: #232323;
    --list-dark: #2b2b2b;
    --list-dark-end: #1c1c1c;
    --silver-light: #e4e4e4;
    --silver-mid: #c2c2c2;
    --silver-dark: #9d9d9d;
    --ink: #1e1e1e;
    --light-text: #f2f2f2;
    --gap-line: #d8d8d8;
  }
  * { box-sizing: border-box; margin: 0; padding: 0; }
  html, body { width: 1200px; height: 1200px; overflow: hidden; }
  body {
    background: var(--stage);
    font-family: "EB Garamond", Georgia, serif;
    position: relative;
  }
  .card { position: absolute; overflow: hidden; }

  /* Mailing side */
  .mailing-side {
    left: 419px; top: 24px; width: 727px; height: 560px;
    background: var(--card-white);
  }
  .plan-photo {
    position: absolute; left: 0; top: 0; width: 352px; height: 160px;
    background: linear-gradient(135deg, #f4f4f4 0%, #dcdcdc 55%, #c9c9cf 100%);
  }
  .mission-panel {
    position: absolute; left: 0; top: 160px; width: 352px; height: 236px;
    background: var(--panel-grey);
    padding: 6px 12px 0 12px;
    color: var(--panel-text);
    font-size: 19.5px; line-height: 24px; letter-spacing: 0.4px; text-align: justify;
  }
  .mission-panel strong { font-weight: 600; letter-spacing: 0.8px; }
  .contact-bar {
    position: absolute; left: 0; top: 396px; width: 352px; height: 70px;
    background: linear-gradient(90deg, var(--bar-dark), var(--bar-dark-end));
  }
  .contact-bar .brand-box {
    position: absolute; left: 8px; top: 6px; width: 92px; height: 58px;
    background: var(--silver-mid);
    display: flex; flex-direction: column; align-items: center; justify-content: center;
    color: var(--ink); text-align: center; font-weight: 600;
  }
  .brand-box .brand-initials { font-size: 22px; line-height: 22px; letter-spacing: 1px; }
  .brand-box .brand-sub { font-size: 9px; line-height: 12px; letter-spacing: 0.3px; }
  .contact-bar .contact-list {
    position: absolute; left: 112px; top: 6px;
    list-style: none; color: var(--light-text); font-size: 17px; line-height: 19px;
  }
  .contact-list li { display: flex; align-items: center; gap: 10px; }
  .contact-list svg { flex: none; }
  .return-address {
    position: absolute; left: 364px; top: 22px; font-style: normal;
    font-size: 13px; line-height: 16px; color: var(--ink);
  }
  .return-address .company { font-size: 17px; font-weight: 600; letter-spacing: 0.6px; line-height: 20px; }
  .stamp-box {
    position: absolute; left: 551px; top: 12px; width: 166px; height: 166px;
    border: 1px solid #9a9a9a;
  }

  /* Promo side */
  .promo-side {
    left: 64px; top: 614px; width: 729px; height: 562px;
    background: var(--gap-line);
  }
  .crew-photo {
    position: absolute; left: 0; top: 0; width: 364px; height: 258px;
    background: linear-gradient(160deg, #8c8a86 0%, #5f5d5a 45%, #7d8a5c 100%);
  }
  .services-panel {
    position: absolute; left: 367px; top: 0; width: 362px; height: 258px;
    background: linear-gradient(180deg, var(--list-dark), var(--list-dark-end));
    padding: 28px 0 0 14px;
    list-style: none; color: var(--light-text);
    font-size: 20px; line-height: 23px;
  }
  .services-panel li::before { content: "\2022\00a0"; }
  .photo-row {
    position: absolute; left: 0; top: 262px; width: 729px; height: 150px;
    display: flex; gap: 4px;
  }
  .photo-row div { flex: 1; height: 100%; }
  .photo-house { background: linear-gradient(180deg, #9fb6cf 0%, #6d7f52 60%, #4d6b33 100%); }
  .photo-kitchen-dark { background: linear-gradient(180deg, #d9d4cc 0%, #3b3632 60%, #6d5437 100%); }
  .photo-kitchen-wood { background: linear-gradient(180deg, #b99663 0%, #6b4526 55%, #3f2d22 100%); }
  .photo-bath { background: linear-gradient(180deg, #e6cf93 0%, #d9b876 55%, #efe6d2 100%); }
  .silver-band {
    position: absolute; left: 0; top: 412px; width: 729px; height: 150px;
    background: linear-gradient(180deg, var(--silver-light) 0%, var(--silver-mid) 55%, var(--silver-dark) 100%);
  }
  .silver-band .brand-name {
    position: absolute; left: 70px; top: 30px; width: 260px; height: 92px;
    display: flex; align-items: center; gap: 14px;
    font-size: 28px; font-weight: 600; color: var(--ink); line-height: 32px;
  }
  .brand-name .brand-square { width: 18px; height: 18px; background: var(--ink); flex: none; }
  .silver-band h2 {
    position: absolute; left: 382px; top: 10px;
    font-size: 35px; font-weight: 400; color: #333; letter-spacing: 0.3px;
  }
  .silver-band .contact-list {
    position: absolute; left: 382px; top: 60px;
    list-style: none; color: #333; font-size: 21px; line-height: 26px;
  }
  .silver-band .contact-list li { gap: 18px; }
</style>
</head>
<body>

<section class="card mailing-side" aria-label="Postcard mailing side">
  <div class="plan-photo" role="img" aria-label="Photo of a compass resting on a floor plan drawing"></div>
  <p class="mission-panel">The success of a new construction project depends on the talent and dedication of the tradespeople whose job it is to bring the project to life. <strong>RLW Construction Co.</strong> has a clear mission that's been driving its success - and the success of its clients - for years. Our goals can be summed up in one simple statement:</p>
  <div class="contact-bar">
    <div class="brand-box"><span class="brand-initials">RLW</span><span class="brand-sub">Construction Co.</span></div>
    <ul class="contact-list">
      <li><svg width="12" height="12" viewBox="0 0 24 24"><path fill="#f2f2f2" d="M6.6 10.8a15 15 0 0 0 6.6 6.6l2.2-2.2c.3-.3.7-.4 1-.2 1.1.4 2.3.6 3.6.6.6 0 1 .4 1 1V20c0 .6-.4 1-1 1A17 17 0 0 1 3 4c0-.6.4-1 1-1h3.5c.6 0 1 .4 1 1 0 1.3.2 2.5.6 3.6.1.3 0 .7-.2 1z"/></svg>617-555-0148</li>
      <li><svg width="12" height="10" viewBox="0 0 24 18"><rect width="24" height="18" fill="#f2f2f2"/><path d="M1 1l11 9 11-9" fill="none" stroke="#2b2b2b" stroke-width="2"/></svg>rlw48@mailbay.net</li>
      <li><svg width="12" height="12" viewBox="0 0 24 24" fill="none" stroke="#f2f2f2" stroke-width="2"><circle cx="12" cy="12" r="10"/><path d="M2 12h20M12 2c3 3 3 17 0 20M12 2c-3 3-3 17 0 20"/></svg>www.rlwconstructionco.com</li>
    </ul>
  </div>
  <address class="return-address">
    <div class="company">R L W Construction Co.</div>
    72 Linden Ct<br>Marlow , MA 02190
  </address>
  <div class="stamp-box"></div>
</section>

<section class="card promo-side" aria-label="Postcard promotional side">
  <div class="crew-photo" role="img" aria-label="Photo of a contractor and a site worker in hard hats reviewing a building site"></div>
  <ul class="services-panel">
    <li>Home improvement &amp; maintenance</li>
    <li>Renovations &amp; repairs</li>
    <li>Bath, Kitchen &amp; Ceramic Remodeling</li>
    <li>Decks, terraces &amp; balconies</li>
    <li>Masonry, roofing &amp; siding</li>
    <li>Interior finish &amp; painting</li>
    <li>Plumbing services</li>
    <li>Electrical work</li>
    <li>and more!</li>
  </ul>
  <div class="photo-row">
    <div class="photo-house" role="img" aria-label="Photo of a brick home with landscaped yard"></div>
    <div class="photo-kitchen-dark" role="img" aria-label="Photo of a modern kitchen with dark cabinets"></div>
    <div class="photo-kitchen-wood" role="img" aria-label="Photo of a kitchen with wood cabinets and pendant lights"></div>
    <div class="photo-bath" role="img" aria-label="Photo of a remodeled bathroom with a soaking tub"></div>
  </div>
  <div class="silver-band">
    <div class="brand-name"><span class="brand-square"></span><span>RLW<br>Construction Co.</span></div>
    <h2>Contact Us Today!</h2>
    <ul class="contact-list">
      <li><svg width="16" height="16" viewBox="0 0 24 24"><path fill="#222" d="M6.6 10.8a15 15 0 0 0 6.6 6.6l2.2-2.2c.3-.3.7-.4 1-.2 1.1.4 2.3.6 3.6.6.6 0 1 .4 1 1V20c0 .6-.4 1-1 1A17 17 0 0 1 3 4c0-.6.4-1 1-1h3.5c.6 0 1 .4 1 1 0 1.3.2 2.5.6 3.6.1.3 0 .7-.2 1z"/></svg>617-555-0148</li>
      <li><svg width="16" height="12" viewBox="0 0 24 18"><rect width="24" height="18" fill="#222"/><path d="M1 1l11 9 11-9" fill="none" stroke="#c2c2c2" stroke-width="2"/></svg>rlw48@mailbay.net</li>
      <li><svg width="16" height="16" viewBox="0 0 24 24" fill="none" stroke="#222" stroke-width="2"><circle cx="12" cy="12" r="10"/><path d="M2 12h20M12 2c3 3 3 17 0 20M12 2c-3 3-3 17 0 20"/></svg>www.rlwconstructionco.com</li>
    </ul>
  </div>
</section>

</body>
</html>
```